【タイトル】
超現実派エンジニアも驚く!
メンタル不調も!恋愛の失敗も!実らない努力も!

全ての原因は56種の「モヤリンk」
最強ワークで過去を手放し、人生を全て好転させよう! 

【書籍の特典情報】
誰でもできる
「セルフ解放ワーク」
の動画プレゼント!

【ターゲット】
引き寄せの法則や成功法則が好きな方向け

【著者】
(元システムエンジニア)
企業サポーター
桐野 沙織

【説明】
電子書籍の表紙のデザインをお願いします。

電子書籍なので、タイトル文字を見やすくしてほしいです。

元システムエンジニアで、企業サポーターという職業柄もあり
とても現実派の私が実感して提供しているワークのお話になります

引き寄せやスピリチュアルとは違うので、
どちらかというと成功の法則のように
現実的なイメージの表紙だと良いかなと思っています。

本文をつけますので参考にしていただければと思います。

見た時に、とてもインパクトがあるように感じました。
電子書籍は、表紙の役割が大きいので
わかりやすさもとても大切だと感じ、選ばせていただきました。

皆様、素敵なデザインをご提案いただきありがとうございます。
とても迷い、投票も行い選択させていただきました。
今後、お仕事やデザインをご依頼させていただく際は
また、よろしくお願いいたします。

```html
<!DOCTYPE html>
<html lang="ja">
<head>
<meta charset="utf-8">
<title>モヤリンk 表紙</title>
<link rel="stylesheet" href="https://fonts.googleapis.com/css2?family=Noto+Sans+JP:wght@500;700;900&display=swap">
<style>
:root{
  --blue:#1d4fd8;
  --navy:#12236b;
  --red:#e3202a;
  --yellow:#fff23a;
  --mist:#d9ebf8;
  --mist-text:#c5dff3;
  --ink:#111111;
  --white:#ffffff;
}
*{margin:0;padding:0;box-sizing:border-box}
html,body{width:752px;height:1200px;overflow:hidden;background:var(--white)}
.cover{position:relative;width:752px;height:1200px;overflow:hidden;background:var(--white);font-family:"Noto Sans JP",sans-serif;font-weight:900}
.abs{position:absolute}
.top-band{left:0;top:0;width:752px;height:100px;background:var(--blue);color:var(--white);font-size:52px;line-height:100px;text-align:center;letter-spacing:1px;white-space:nowrap}
.halo{left:150px;top:270px;width:560px;height:560px;border-radius:50%;background:var(--mist)}
.ghost-word{left:10px;font-family:"Noto Sans JP",sans-serif;font-weight:900;font-style:italic;color:var(--mist-text);font-size:150px;line-height:1;letter-spacing:-4px;white-space:nowrap}
.tag{top:112px;width:218px;height:140px;background:var(--yellow);border-radius:22px;color:var(--red);font-size:44px;line-height:56px;text-align:center;display:flex;align-items:center;justify-content:center;white-space:nowrap}
.minus-mark{left:34px;top:262px}
.cause-line{left:30px;top:300px;width:700px;text-align:center;color:var(--ink);font-size:68px;line-height:110px;white-space:nowrap}
.cause-line .num{font-size:112px;color:var(--ink);vertical-align:-6px}
.title-name{left:0;top:430px;width:752px;text-align:center;color:var(--blue);font-size:122px;line-height:160px;letter-spacing:-2px;white-space:nowrap}
.promise{left:0;width:752px;text-align:center;color:var(--navy);font-size:58px;line-height:76px;white-space:nowrap}
.promise em{font-style:normal;color:var(--red)}
.plus-mark{left:696px;top:770px}
.bottom-band{left:0;top:850px;width:752px;height:350px;background:var(--blue)}
.bonus-label{left:40px;top:868px;width:268px;height:46px;background:var(--red);color:var(--white);font-size:30px;line-height:46px;text-align:center;border-radius:8px;z-index:2}
.bonus-box{left:30px;top:922px;width:288px;height:250px;background:var(--yellow);border-radius:26px;color:var(--red);font-size:27px;line-height:44px;text-align:center;display:flex;align-items:center;justify-content:center;white-space:nowrap;padding-top:6px}
.cheer{left:338px;top:884px;width:390px;height:62px;background:var(--white);color:var(--navy);font-size:34px;font-weight:700;line-height:62px;text-align:center;white-space:nowrap}
.author-role{left:338px;top:978px;width:390px;text-align:center;color:var(--white);font-size:32px;font-weight:700;line-height:46px;white-space:nowrap}
.author-name{left:338px;top:1068px;width:390px;text-align:center;color:var(--white);font-size:72px;font-weight:700;line-height:90px;letter-spacing:8px;white-space:nowrap}
.author-roman{left:338px;top:1160px;width:390px;text-align:center;color:var(--white);font-size:24px;font-weight:500;letter-spacing:6px;line-height:30px;white-space:nowrap}
</style>
</head>
<body>
<div class="cover">
  <div class="abs top-band">超現実派エンジニアも驚く！</div>

  <div class="abs halo"></div>
  <div class="abs ghost-word" style="top:440px">moyarin</div>
  <div class="abs ghost-word" style="top:590px">energy</div>

  <div class="abs tag" style="left:20px">メンタル<br>不調も！</div>
  <div class="abs tag" style="left:267px">恋愛の<br>失敗も！</div>
  <div class="abs tag" style="left:514px">実らない<br>努力も！</div>

  <svg class="abs minus-mark" width="50" height="50" viewBox="0 0 50 50" aria-hidden="true">
    <circle cx="25" cy="25" r="24" fill="var(--navy)"/>
    <rect x="11" y="21" width="28" height="8" rx="2" fill="var(--white)"/>
  </svg>

  <div class="abs cause-line">全ての原因は<span class="num">56</span>種の</div>
  <div class="abs title-name">「モヤリンk」</div>

  <div class="abs promise" style="top:690px"><em>最強ワーク</em>で過去を手放し</div>
  <div class="abs promise" style="top:768px">人生を全て<em>好転</em>させよう！</div>

  <svg class="abs plus-mark" width="44" height="44" viewBox="0 0 44 44" aria-hidden="true">
    <circle cx="22" cy="22" r="21" fill="var(--red)"/>
    <rect x="18" y="9" width="8" height="26" fill="var(--white)"/>
    <rect x="9" y="18" width="26" height="8" fill="var(--white)"/>
  </svg>

  <div class="abs bottom-band"></div>
  <div class="abs bonus-box">誰でもできる<br>「セルフ解放ワーク」<br>の動画プレゼント！</div>
  <div class="abs bonus-label">読者特典</div>

  <div class="abs cheer">素敵な人生を応援します</div>
  <div class="abs author-role">元システムエンジニア<br>企業サポーター</div>
  <div class="abs author-name">桐野 沙織</div>
  <div class="abs author-roman">KIRINO SAORI</div>
</div>
</body>
</html>
```